Business Card Design Project

Need a business card designed for a horse racing/gambling centered company.
Company name is BrightQuill.com.au
Company colours are similar to those in the logo.
Something clean and modern , designer given liberty to be creative.
Incorporate the logo is preferred.
Single or Double Sided fine
Must include :
Name
Mobile Number
Email Address
Reason: Apologies, I have been traveling unexpectedly with business and just need the extra two days to reply and give feedback before making a decision.
Industry/Entity Type
Business

```html
<!DOCTYPE html>
<html lang="en">
<head>
<meta charset="utf-8">
<title>BrightQuill.com.au Business Card</title>
<link href="https://fonts.googleapis.com/css2?family=Share+Tech&display=swap" rel="stylesheet">
<style>
  :root {
    --teal: #0c8f8a;
    --teal-light: #4fb9b4;
    --teal-deep: #077a75;
    --white: #ffffff;
    --backdrop: #efeae2;
  }
  html, body {
    margin: 0;
    padding: 0;
    width: 1200px;
    height: 900px;
    overflow: hidden;
    background: var(--backdrop);
    font-family: "Share Tech", sans-serif;
  }
  .canvas {
    position: relative;
    width: 1200px;
    height: 900px;
  }
  .card {
    position: absolute;
    left: 290px;
    width: 592px;
    height: 361px;
    overflow: hidden;
    box-shadow: 0 4px 10px rgba(0,0,0,0.25);
  }
  .card-front {
    top: 67px;
    background: radial-gradient(circle at 60% 25%, var(--teal-light) 0%, var(--teal) 45%, var(--teal-deep) 100%);
  }
  .card-back {
    top: 451px;
    background: var(--white);
  }
  .card-back .diagonal {
    position: absolute;
    inset: 0;
  }
  .brand-mark {
    position: absolute;
    display: flex;
    flex-direction: column;
    align-items: center;
    gap: 14px;
  }
  .brand-mark .disc {
    border-radius: 50%;
    background: var(--white);
  }
  .brand-mark .brand-name {
    color: var(--white);
    letter-spacing: 2px;
    white-space: nowrap;
  }
  .card-front .brand-mark {
    left: 0;
    right: 0;
    top: 58px;
  }
  .card-front .disc {
    width: 190px;
    height: 190px;
  }
  .card-front .brand-name {
    font-size: 30px;
  }
  .card-back .brand-mark {
    left: 20px;
    top: 22px;
    width: 190px;
  }
  .card-back .disc {
    width: 150px;
    height: 150px;
    background: var(--teal);
  }
  .card-back .brand-name {
    color: var(--teal);
    font-size: 20px;
  }
  .contact {
    position: absolute;
    right: 20px;
    bottom: 28px;
    margin: 0;
    text-align: right;
    color: var(--white);
    font-size: 17px;
    line-height: 23px;
    letter-spacing: 2px;
    font-variant: small-caps;
  }
  .contact p { margin: 0; }
</style>
</head>
<body>
<main class="canvas">
  <section class="card card-front">
    <div class="brand-mark">
      <div class="disc"></div>
      <span class="brand-name">BrightQuill.com.au</span>
    </div>
  </section>

  <section class="card card-back">
    <svg class="diagonal" width="592" height="361" viewBox="0 0 592 361" aria-hidden="true">
      <defs>
        <radialGradient id="band-glow" cx="0.3" cy="0.85" r="0.7">
          <stop offset="0" stop-color="#6cc3bf"/>
          <stop offset="0.45" stop-color="#0c8f8a"/>
          <stop offset="1" stop-color="#0a8a85"/>
        </radialGradient>
      </defs>
      <polygon points="592,0 592,361 0,361 0,355" fill="#3aa8a3"/>
      <polygon points="592,8 592,361 12,361" fill="url(#band-glow)"/>
    </svg>
    <div class="brand-mark">
      <div class="disc"></div>
      <span class="brand-name">BrightQuill.com.au</span>
    </div>
    <div class="contact">
      <p>Name: Daniel Harper</p>
      <p>Phone : 0412555093</p>
      <p>Email: Daniel@brightquill.com.au</p>
    </div>
  </section>
</main>
</body>
</html>
```